Business Card Design

I'm a young beekeeper (22 years old) just starting out. I own and run 80 hives and would like to eventually build up to 1000. My aim is to run it in tandem with our family farm that is currently running sheep and beef. Unlike a number of honey companies on the East Coast (or the North Island, NZ) I am local and will expand onto the lease blocks that our family is also leasing. I want a simple plain logo/photo. The designer may wish to use one of the photos as a background outline or however they chose. The mountain is Aorangi and our farm borders one side of it.

Target Market(s)

From local land owners to wholesale honey buyers

Industry/Entity Type

Farm

Contact Information for Business Card

Pekeriu Honey
Manager Owner Manaia Brooks
email pekeriuhoney@tuimailbox.co.nz
mobile 0217394461

Requirements
Must have
• The details submitted. The brand Pekeriu Honey to be the main feature. The other details can be smaller.
Should not have
• Must not include a picture of a bee or hive. Use a modern font. Don't use koru but may incorporate poutama.

```html
<!DOCTYPE html>
<html lang="en">
<head>
<meta charset="utf-8">
<title>Pekeriu Honey — Business Card</title>
<link rel="stylesheet" href="https://fonts.googleapis.com/css2?family=Source+Sans+3:wght@400&display=swap">
<style>
  :root {
    --paper: #f1efea;
    --paper-edge: #e6e3dc;
    --ink: #3f3f3f;
    --amber: #f2b01e;
    --amber-soft: #f3e3b8;
    --stone: #d9d7d2;
    --stone-line: #cfcdc8;
  }
  * { margin: 0; padding: 0; box-sizing: border-box; }
  html, body {
    width: 1200px;
    height: 741px;
    overflow: hidden;
    background: var(--paper);
  }
  .card {
    position: relative;
    width: 1200px;
    height: 741px;
    overflow: hidden;
    background: radial-gradient(ellipse at 45% 40%, var(--paper) 0%, var(--paper) 55%, var(--paper-edge) 100%);
    font-family: "Source Sans 3", sans-serif;
    color: var(--ink);
  }
  .brand {
    position: absolute;
    left: 82px;
    top: 292px;
    display: flex;
    align-items: center;
    gap: 20px;
  }
  .brand__mark {
    width: 40px;
    height: 40px;
    background: var(--amber);
  }
  .brand__name {
    font-size: 58px;
    font-weight: 400;
    color: var(--amber);
    line-height: 1;
    letter-spacing: 0.5px;
  }
  .accent-block {
    position: absolute;
    left: 900px;
    top: 420px;
    width: 230px;
    height: 230px;
    background: var(--stone);
    border: 3px solid var(--stone-line);
    opacity: 0.7;
  }
  .person {
    position: absolute;
    left: 659px;
    top: 172px;
  }
  .person__name {
    font-size: 56px;
    font-weight: 400;
    line-height: 1;
  }
  .person__role {
    margin-top: 10px;
    margin-left: 9px;
    font-size: 30px;
    font-weight: 400;
    line-height: 1;
  }
  .contact {
    position: absolute;
    left: 104px;
    top: 528px;
    list-style: none;
  }
  .contact__item {
    display: flex;
    align-items: center;
    height: 40px;
    margin-bottom: 25px;
    font-size: 32px;
    line-height: 1;
  }
  .contact__icon {
    width: 42px;
    height: 36px;
    margin-right: 25px;
    flex: none;
  }
</style>
</head>
<body>
  <main class="card">
    <div class="brand">
      <span class="brand__mark"></span>
      <span class="brand__name">Pekeriu Honey</span>
    </div>

    <div class="accent-block" aria-hidden="true"></div>

    <div class="person">
      <h1 class="person__name">Manaia Brooks</h1>
      <p class="person__role">Manager\Owner</p>
    </div>

    <ul class="contact">
      <li class="contact__item">
        <svg class="contact__icon" viewBox="0 0 42 36" aria-hidden="true">
          <rect x="2" y="6" width="38" height="24" fill="none" stroke="#3f3f3f" stroke-width="2.5"/>
          <polyline points="2,6 21,21 40,6" fill="none" stroke="#3f3f3f" stroke-width="2.5"/>
          <line x1="2" y1="30" x2="16" y2="17" stroke="#3f3f3f" stroke-width="2.5"/>
          <line x1="40" y1="30" x2="26" y2="17" stroke="#3f3f3f" stroke-width="2.5"/>
        </svg>
        <span>pekeriuhoney@tuimailbox.co.nz</span>
      </li>
      <li class="contact__item">
        <svg class="contact__icon" viewBox="0 0 42 36" aria-hidden="true">
          <path d="M10 3 L16 3 L18 10 L14 13 C15.5 19 19 23.5 24 26 L27 22 L34 24 L34 30 C33 33 30 34 27 33 C17 30 9 21 7 10 C6.5 6 8 3.5 10 3 Z" fill="#3f3f3f"/>
        </svg>
        <span>0217394461</span>
      </li>
    </ul>
  </main>
</body>
</html>
```